Logo Design and Business Card Musician

I need a design for a Business Card and a logo for a professional of music industry. His name is Marco Vilaseca: composer, arranger and music producer. You can find him in: [login to view URL], although we are now working in some many changes regarding the site environment. The logo can be with the initials M V, M Vi or any other external suggestion. I request (my idea is, but I am so open), three basic colors: black and white (in any combination) and a different colour. Business card will be two faces: the backside with the link to the web and the logo. Marco Vilaseca: composer with experience working with artists, tv, theatre… Some adjectives of his personality: direct, energetic, resolute, fresh, his music is a reflect of his personality. No interest in "obvious" symbols like treble clef, a piano… Thank you very much.

Necesito un diseño de una Business Card y el Logo para un profesional del mundo de la música. El nombre es Marco Vilaseca: compositor, arreglista y productor musical. Puedes encontrarlo en [login to view URL], aunque estamos en fase de cambio del entorno de la web. Puede tratarse de un logo con las iniciales M V, M Vi o cualquier sugerencia externa. Solicito, en principio, tres colores básicos: negro y blanco (en cualquier combinación) y un color. La Business card será a dos caras: en la trasera irá solo la web y el logo. Marco Vilaseca: compositor con experiencia en artistas, televisión, teatro… directo, contundente, enérgico, fresco, su música es reflejo de su personalidad. No estoy muy interesada en símbolos "obvios" como clave de sol, teclas del piano… Muchas gracias.

```html
<!DOCTYPE html>
<html lang="en">
<head>
<meta charset="utf-8">
<title>Marco Vilaseca — Business Card</title>
<link href="https://fonts.googleapis.com/css2?family=Cinzel:wght@400&family=Open+Sans:wght@400;600;700&display=swap" rel="stylesheet">
<style>
  :root {
    --orange: #e8621a;
    --orange-dark: #c9511a;
    --white: #ffffff;
    --paper: #ece9e4;
    --tab: #e3e1de;
    --text-orange: #e0581a;
  }
  * { box-sizing: border-box; margin: 0; padding: 0; }
  html, body {
    width: 1200px; height: 873px; overflow: hidden;
    background: var(--paper);
    font-family: "Open Sans", Arial, sans-serif;
  }
  .canvas { position: relative; width: 1200px; height: 873px; }

  .card {
    position: absolute; left: 290px; width: 620px; height: 354px;
    box-shadow: 0 6px 18px rgba(0,0,0,.12);
    overflow: hidden;
  }
  .card-front { top: 52px; background: var(--white); }
  .card-back { top: 466px; background: var(--orange); }

  /* front */
  .rule { position: absolute; left: 0; right: 0; height: 2px; background: var(--orange); }
  .rule-top { top: 22px; }
  .rule-bottom { bottom: 22px; }

  .monogram {
    position: absolute; left: 30px; top: 70px; width: 260px;
    text-align: center; color: var(--orange);
    font-weight: 700; font-size: 104px; line-height: 1; letter-spacing: -0.02em;
  }
  .wordmark {
    position: absolute; left: 20px; top: 222px; width: 280px;
    text-align: center; color: var(--orange);
    font-family: "Cinzel", Georgia, serif; font-size: 21px; letter-spacing: .16em;
  }

  .title-bar {
    position: absolute; left: 322px; top: 62px; width: 282px; height: 44px;
    background: var(--orange); color: var(--white); text-align: center;
    padding-top: 5px;
  }
  .title-bar .name { font-weight: 700; font-size: 16px; line-height: 19px; }
  .title-bar .role { font-size: 8.5px; font-weight: 600; letter-spacing: .02em; }

  .contacts { position: absolute; left: 322px; top: 120px; list-style: none; }
  .contact { display: flex; align-items: flex-start; height: 38px; }
  .contact .tab {
    flex: none; width: 34px; height: 28px; background: var(--tab);
    display: flex; align-items: center; justify-content: flex-end; padding-right: 4px;
  }
  .contact .icon {
    width: 20px; height: 20px; border-radius: 50%; background: var(--orange);
    color: var(--white); font-size: 10px; font-weight: 700;
    display: flex; align-items: center; justify-content: center;
  }
  .contact .icon svg { width: 12px; height: 12px; }
  .contact .value {
    margin-left: 10px; padding-top: 5px;
    color: var(--text-orange); font-size: 12px; line-height: 15px; white-space: nowrap;
  }

  /* back */
  .back-art {
    position: absolute; inset: 0;
    background:
      radial-gradient(circle at 80% 30%, var(--orange-dark) 0, transparent 38%),
      radial-gradient(circle at 20% 35%, var(--orange-dark) 0, transparent 40%),
      radial-gradient(circle at 75% 85%, var(--orange-dark) 0, transparent 30%),
      var(--orange);
    opacity: .85;
  }
  .back-monogram {
    position: absolute; left: 0; right: 0; top: 58px; text-align: center;
    color: var(--white); font-weight: 700; font-size: 170px; line-height: 1;
    letter-spacing: -0.02em;
  }
  .back-url {
    position: absolute; left: 0; right: 0; top: 272px; text-align: center;
    color: var(--white); font-size: 21px; letter-spacing: .1em;
  }
</style>
</head>
<body>
<main class="canvas">

  <section class="card card-front" aria-label="Business card front">
    <div class="rule rule-top"></div>
    <div class="rule rule-bottom"></div>

    <div class="monogram">M V</div>
    <div class="wordmark">MARCO VILASECA</div>

    <div class="title-bar">
      <div class="name">Marco Vilaseca</div>
      <div class="role">COMPOSER, ARRANGER &amp; MUSIC PRODUCER</div>
    </div>

    <ul class="contacts">
      <li class="contact">
        <span class="tab"><span class="icon">M</span></span>
        <span class="value">000 . 4821 .3907</span>
      </li>
      <li class="contact">
        <span class="tab"><span class="icon">E</span></span>
        <span class="value">marcovilasecamusic@notesmail.net</span>
      </li>
      <li class="contact">
        <span class="tab"><span class="icon">
          <svg viewBox="0 0 12 12" fill="none" stroke="#fff" stroke-width="1">
            <circle cx="6" cy="6" r="5"/>
            <ellipse cx="6" cy="6" rx="2.2" ry="5"/>
            <line x1="1" y1="6" x2="11" y2="6"/>
          </svg>
        </span></span>
        <span class="value">www.marcovilasecasound.net</span>
      </li>
      <li class="contact">
        <span class="tab"><span class="icon">
          <svg viewBox="0 0 12 12" fill="#fff">
            <path d="M6 1 L11 6 L9.5 6 L9.5 11 L7 11 L7 8 L5 8 L5 11 L2.5 11 L2.5 6 L1 6 Z"/>
          </svg>
        </span></span>
        <span class="value">120 Harbor Lane<br>Easton, NY 10482</span>
      </li>
    </ul>
  </section>

  <section class="card card-back" aria-label="Business card back">
    <div class="back-art" role="img" aria-label="Faint tone-on-tone illustration of piano keys, music staff with notes, headphones, sound wave bars and a vintage microphone"></div>
    <div class="back-monogram">M V</div>
    <div class="back-url">www.marcovilasecasound.net</div>
  </section>

</main>
</body>
</html>
```